Web design for Marketplace

Guys!
1st of all, thank you for willing to help me out.
I have attached PDF file with examples.
I am looking for professional and clean design for my new project “ Lantern of Seers “. Its marketplace for Psychic Readers around the world. Where they will able to register to provide their services via Chat,Email and sell their products on their personal stores.
Customer will able to get services and buy products from Psychic on Marketplace.
url : http://www.lanternofseers-demo.net
Please note: it doesn’t matter, what my current site looks like. I am looking for completely new design.
It doesn't matter if you add or remove : Clipvale video or even text which is on the home page in new design.
Following are the main pages of the website, which i am looking to be design.
1. Home page
2. Psychic
3. Marketplace
4. Psychic profile page
5. Psychic Store page
6. Psychic product page
7. Logo
following is the website, which i like the most. I would love to have something like that. It is neat , clean and friendly. I am looking for depth in design and neatness and borders (matter and a lot and it should be prefect ).
http://www.craftnook-demo.net
P.S : i believe it will be helpful to choose one of you. If you can only create design of " Homepage" at 1st , so i can go ahead and hire one of you guys.
Best,
Hi guys!
Guys,

```html
<!DOCTYPE html>
<html lang="en">
<head>
<meta charset="utf-8">
<title>Lantern of Seers — Home</title>
<link href="https://fonts.googleapis.com/css2?family=Open+Sans:wght@400;600;700&family=Oswald:wght@400;500&display=swap" rel="stylesheet">
<style>
:root{
  --page:#f1f2f4;
  --card:#ffffff;
  --ink:#333333;
  --muted:#8a8a8a;
  --rule:#e2e3e6;
  --accent:#ec5a10;
  --nav-top:#3ea9e6;
  --nav-bottom:#1a86c9;
  --nav-edge:#1677b4;
  --search:#5bb8ec;
  --go-top:#ffa31a;
  --go-bottom:#f07800;
  --star:#f4c430;
  --star-off:#d6d6d6;
  --photo:#a68670;
  --spell:#9b1420;
  --spell-light:#e7b7ba;
  --video:#6b5a4c;
  --join-top:#3aa0dc;
  --join-bottom:#1877b7;
}
*{margin:0;padding:0;box-sizing:border-box}
html,body{width:729px;height:1200px;overflow:hidden;background:var(--page)}
body{font-family:"Open Sans",Arial,sans-serif;color:var(--ink);font-size:11px}
.page{position:relative;width:729px;height:1200px}
.abs{position:absolute}

/* header */
.account-links{left:585px;top:4px;font-size:8px;color:#555}
.account-links span{margin:0 3px;color:#999}
.brand{left:97px;top:12px;display:flex;align-items:center;gap:5px;font-weight:700;font-size:14px;color:#222}
.brand-mark{width:12px;height:12px;background:var(--accent)}
.main-nav{left:97px;top:57px;width:535px;height:27px;border-radius:2px;background:linear-gradient(var(--nav-top),var(--nav-bottom));border-bottom:1px solid var(--nav-edge);display:flex;align-items:center;color:#fff;font-size:10px}
.nav-item{height:100%;display:flex;align-items:center;padding:0 10px;border-right:1px solid rgba(0,0,0,.15);box-shadow:1px 0 0 rgba(255,255,255,.2)}
.search{margin-left:10px;width:271px;height:17px;background:var(--search);border-radius:2px;display:flex;align-items:center;justify-content:space-between;font-style:italic;font-size:8px;color:#e9f5fc;padding-left:8px}
.search-go{width:27px;height:16px;background:linear-gradient(var(--go-top),var(--go-bottom));border-radius:2px;font-style:normal;font-weight:700;color:#fff;text-align:center;line-height:16px;font-size:9px}
.nav-help{margin-left:auto;padding:0 16px;border-left:1px solid rgba(0,0,0,.15)}

/* section headings */
.section-title{font-weight:700;font-size:11px;color:#222;display:flex;align-items:center;gap:10px}
.section-title::after{content:"";flex:1;height:4px;background:var(--rule)}

/* psychic cards */
.psychic-card{width:262px;height:120px;background:var(--card);box-shadow:0 1px 3px rgba(0,0,0,.12)}
.psychic-card::after{content:"";position:absolute;left:0;right:0;bottom:0;height:3px;background:#dcdcdc}
.psychic-photo{left:9px;top:9px;width:61px;height:67px;background:linear-gradient(#c8b3a4,var(--photo))}
.psychic-rate{left:0;width:79px;top:81px;text-align:center;color:var(--accent);font-size:7px}
.chat-icon{left:27px;top:100px}
.psychic-name{left:83px;top:7px;color:var(--accent);font-weight:700;font-size:9px}
.psychic-stars{left:82px;top:20px}
.psychic-country{right:11px;top:6px;color:var(--muted);font-size:7px}
.psychic-bio{left:83px;top:42px;font-size:7px;line-height:11.5px;color:#444}
.more{color:var(--accent);font-weight:600}

/* marketplace */
.product{width:92px;height:92px;background:var(--card);box-shadow:0 1px 2px rgba(0,0,0,.08)}
.product-art{left:5px;top:6px;width:84px;height:59px;background:radial-gradient(ellipse at center,var(--spell-light) 0,#c2414b 45%,var(--spell) 80%)}
.product-name{left:7px;top:69px;font-size:7px;color:#222}
.product-meta{left:7px;top:79px;width:80px;font-size:7px;display:flex;justify-content:space-between;color:var(--muted)}
.product-meta b{font-weight:400;color:var(--accent)}

/* sidebar */
.side-box{left:496px;width:137px;background:#f8f8f9;border:1px solid #dcdcdf;box-shadow:0 1px 2px rgba(0,0,0,.06)}
.side-title{font-weight:700;color:#222}
.newsletter-title{left:9px;top:8px;font-size:11px}
.side-rule{height:2px;background:var(--rule)}
.newsletter-copy{left:9px;top:45px;font-size:6.5px;line-height:10px;color:#555}
.email-field{left:8px;top:70px;width:118px;height:15px;background:#fff;border:1px solid #d6d6d6;font-style:italic;font-size:6.5px;color:#aaa;padding:3px 5px}
.btn-submit{left:8px;top:96px;width:52px;height:15px;border-radius:2px;background:linear-gradient(var(--go-top),var(--go-bottom));color:#fff;font-weight:700;font-size:8px;text-align:center;line-height:15px}
.video-title{left:9px;top:6px;width:120px;font-size:7.5px;line-height:11px}
.video-thumb{left:9px;top:41px;width:117px;height:86px;background:linear-gradient(135deg,#8c7a6a,var(--video) 60%,#3c332c)}
.video-copy{left:9px;top:146px;font-size:7px;line-height:10px;color:#555}
.join-avatar{left:51px;top:15px;width:33px;height:33px;border-radius:50%;background:#d9dadd}
.join-title{left:0;width:100%;top:58px;text-align:center;font-family:"Oswald",Arial,sans-serif;font-size:16px;color:#222}
.join-copy{left:0;width:100%;top:89px;text-align:center;font-size:7px;line-height:10px;color:#555;padding:0 12px}
.join-copy strong{display:block;font-weight:400;color:#1e88c8;font-size:9px;line-height:12px}
.btn-join{left:22px;top:163px;width:92px;height:20px;border-radius:2px;background:linear-gradient(var(--join-top),var(--join-bottom));color:#fff;font-family:"Oswald",Arial,sans-serif;font-size:11px;text-align:center;line-height:20px}

/* about */
.about-copy{left:99px;top:936px;width:390px;font-size:7.6px;line-height:13px;color:#444}
.about-copy p{margin-bottom:13px}

/* footer */
.footer-rule{left:97px;top:1139px;width:535px;height:2px;background:#e0e1e4}
.footer-links{left:0;width:729px;top:1152px;text-align:center;font-size:7px;color:#777}
.footer-links span{margin:0 4px;color:#aaa}
.footer-copy{left:0;width:729px;top:1166px;text-align:center;font-size:6.5px;color:#999}
</style>
</head>
<body>
<svg width="0" height="0" style="position:absolute">
  <defs>
    <symbol id="star" viewBox="0 0 10 10"><path d="M5 .4l1.4 3 3.2.3-2.4 2.2.7 3.2L5 7.5 2.1 9.1l.7-3.2L.4 3.7l3.2-.3z"/></symbol>
    <symbol id="bubble" viewBox="0 0 16 12"><path d="M1 1h10v6H5l-3 2V7H1z" fill="#c9c9c9"/><path d="M6 4h9v6h-1v2l-3-2H6z" fill="#b5b5b5"/></symbol>
  </defs>
</svg>

<div class="page">
  <header>
    <div class="abs account-links">Login<span>|</span>Signup</div>
    <div class="abs brand"><span class="brand-mark"></span>Lantern of Seers</div>
    <nav class="abs main-nav">
      <div class="nav-item">Psychics</div>
      <div class="nav-item">Marketplace</div>
      <div class="nav-item">My account</div>
      <div class="search">Search Psychic<span class="search-go">GO</span></div>
      <div class="nav-item nav-help">Help</div>
    </nav>
  </header>

  <section class="top-psychics">
    <h2 class="abs section-title" style="left:97px;top:100px;width:535px">Top Pyschics</h2>

    <article class="abs psychic-card" style="left:97px;top:129px">
      <div class="abs psychic-photo" role="img" aria-label="Portrait photo of the psychic"></div>
      <div class="abs psychic-rate">$5.00 / Min</div>
      <svg class="abs chat-icon" width="16" height="12"><use href="#bubble"/></svg>
      <div class="abs psychic-name">Ravel</div>
      <svg class="abs psychic-stars" width="56" height="11" fill="var(--star)"><use href="#star" width="10" height="10"/><use href="#star" x="11" width="10" height="10"/><use href="#star" x="22" width="10" height="10"/><use href="#star" x="33" width="10" height="10"/><use href="#star" x="44" width="10" height="10" fill="var(--star-off)"/></svg>
      <div class="abs psychic-country">United States</div>
      <p class="abs psychic-bio">A study attempted to repeat recently<br>reported parapsychological experiments that<br>appeared to support the existence of<br>precognition. All attempts to repeat the<br>results "failed to produce significant effects",<br><span class="more">more »</span></p>
    </article>
    <article class="abs psychic-card" style="left:370px;top:129px">
      <div class="abs psychic-photo" role="img" aria-label="Portrait photo of the psychic"></div>
      <div class="abs psychic-rate">$5.00 / Min</div>
      <svg class="abs chat-icon" width="16" height="12"><use href="#bubble"/></svg>
      <div class="abs psychic-name">Ravel</div>
      <svg class="abs psychic-stars" width="56" height="11" fill="var(--star)"><use href="#star" width="10" height="10"/><use href="#star" x="11" width="10" height="10"/><use href="#star" x="22" width="10" height="10"/><use href="#star" x="33" width="10" height="10"/><use href="#star" x="44" width="10" height="10" fill="var(--star-off)"/></svg>
      <div class="abs psychic-country">United States</div>
      <p class="abs psychic-bio">A study attempted to repeat recently<br>reported parapsychological experiments that<br>appeared to support the existence of<br>precognition. All attempts to repeat the<br>results "failed to produce significant effects",<br><span class="more">more »</span></p>
    </article>
    <article class="abs psychic-card" style="left:97px;top:266px">
      <div class="abs psychic-photo" role="img" aria-label="Portrait photo of the psychic"></div>
      <div class="abs psychic-rate">$5.00 / Min</div>
      <svg class="abs chat-icon" width="16" height="12"><use href="#bubble"/></svg>
      <div class="abs psychic-name">Ravel</div>
      <svg class="abs psychic-stars" width="56" height="11" fill="var(--star)"><use href="#star" width="10" height="10"/><use href="#star" x="11" width="10" height="10"/><use href="#star" x="22" width="10" height="10"/><use href="#star" x="33" width="10" height="10"/><use href="#star" x="44" width="10" height="10" fill="var(--star-off)"/></svg>
      <div class="abs psychic-country">United States</div>
      <p class="abs psychic-bio">A study attempted to repeat recently<br>reported parapsychological experiments that<br>appeared to support the existence of<br>precognition. All attempts to repeat the<br>results "failed to produce significant effects",<br><span class="more">more »</span></p>
    </article>
    <article class="abs psychic-card" style="left:370px;top:266px">
      <div class="abs psychic-photo" role="img" aria-label="Portrait photo of the psychic"></div>
      <div class="abs psychic-rate">$5.00 / Min</div>
      <svg class="abs chat-icon" width="16" height="12"><use href="#bubble"/></svg>
      <div class="abs psychic-name">Ravel</div>
      <svg class="abs psychic-stars" width="56" height="11" fill="var(--star)"><use href="#star" width="10" height="10"/><use href="#star" x="11" width="10" height="10"/><use href="#star" x="22" width="10" height="10"/><use href="#star" x="33" width="10" height="10"/><use href="#star" x="44" width="10" height="10" fill="var(--star-off)"/></svg>
      <div class="abs psychic-country">United States</div>
      <p class="abs psychic-bio">A study attempted to repeat recently<br>reported parapsychological experiments that<br>appeared to support the existence of<br>precognition. All attempts to repeat the<br>results "failed to produce significant effects",<br><span class="more">more »</span></p>
    </article>
    <article class="abs psychic-card" style="left:97px;top:405px">
      <div class="abs psychic-photo" role="img" aria-label="Portrait photo of the psychic"></div>
      <div class="abs psychic-rate">$5.00 / Min</div>
      <svg class="abs chat-icon" width="16" height="12"><use href="#bubble"/></svg>
      <div class="abs psychic-name">Ravel</div>
      <svg class="abs psychic-stars" width="56" height="11" fill="var(--star)"><use href="#star" width="10" height="10"/><use href="#star" x="11" width="10" height="10"/><use href="#star" x="22" width="10" height="10"/><use href="#star" x="33" width="10" height="10"/><use href="#star" x="44" width="10" height="10" fill="var(--star-off)"/></svg>
      <div class="abs psychic-country">United States</div>
      <p class="abs psychic-bio">A study attempted to repeat recently<br>reported parapsychological experiments that<br>appeared to support the existence of<br>precognition. All attempts to repeat the<br>results "failed to produce significant effects",<br><span class="more">more »</span></p>
    </article>
    <article class="abs psychic-card" style="left:370px;top:405px">
      <div class="abs psychic-photo" role="img" aria-label="Portrait photo of the psychic"></div>
      <div class="abs psychic-rate">$5.00 / Min</div>
      <svg class="abs chat-icon" width="16" height="12"><use href="#bubble"/></svg>
      <div class="abs psychic-name">Ravel</div>
      <svg class="abs psychic-stars" width="56" height="11" fill="var(--star)"><use href="#star" width="10" height="10"/><use href="#star" x="11" width="10" height="10"/><use href="#star" x="22" width="10" height="10"/><use href="#star" x="33" width="10" height="10"/><use href="#star" x="44" width="10" height="10" fill="var(--star-off)"/></svg>
      <div class="abs psychic-country">United States</div>
      <p class="abs psychic-bio">A study attempted to repeat recently<br>reported parapsychological experiments that<br>appeared to support the existence of<br>precognition. All attempts to repeat the<br>results "failed to produce significant effects",<br><span class="more">more »</span></p>
    </article>
  </section>

  <section class="marketplace">
    <h2 class="abs section-title" style="left:99px;top:556px;width:388px">Marketplace</h2>

    <div class="abs product" style="left:97px;top:588px"><div class="abs product-art" role="img" aria-label="Love Spells product artwork with a glowing heart"></div><div class="abs product-name">Love Spell</div><div class="abs product-meta">psychic<b>$200.00</b></div></div>
    <div class="abs product" style="left:196px;top:588px"><div class="abs product-art" role="img" aria-label="Love Spells product artwork with a glowing heart"></div><div class="abs product-name">Love Spell</div><div class="abs product-meta">psychic<b>$200.00</b></div></div>
    <div class="abs product" style="left:295px;top:588px"><div class="abs product-art" role="img" aria-label="Love Spells product artwork with a glowing heart"></div><div class="abs product-name">Love Spell</div><div class="abs product-meta">psychic<b>$200.00</b></div></div>
    <div class="abs product" style="left:394px;top:588px"><div class="abs product-art" role="img" aria-label="Love Spells product artwork with a glowing heart"></div><div class="abs product-name">Love Spell</div><div class="abs product-meta">psychic<b>$200.00</b></div></div>

    <div class="abs product" style="left:97px;top:691px"><div class="abs product-art" role="img" aria-label="Love Spells product artwork with a glowing heart"></div><div class="abs product-name">Love Spell</div><div class="abs product-meta">psychic<b>$200.00</b></div></div>
    <div class="abs product" style="left:196px;top:691px"><div class="abs product-art" role="img" aria-label="Love Spells product artwork with a glowing heart"></div><div class="abs product-name">Love Spell</div><div class="abs product-meta">psychic<b>$200.00</b></div></div>
    <div class="abs product" style="left:295px;top:691px"><div class="abs product-art" role="img" aria-label="Love Spells product artwork with a glowing heart"></div><div class="abs product-name">Love Spell</div><div class="abs product-meta">psychic<b>$200.00</b></div></div>
    <div class="abs product" style="left:394px;top:691px"><div class="abs product-art" role="img" aria-label="Love Spells product artwork with a glowing heart"></div><div class="abs product-name">Love Spell</div><div class="abs product-meta">psychic<b>$200.00</b></div></div>

    <div class="abs product" style="left:97px;top:795px"><div class="abs product-art" role="img" aria-label="Love Spells product artwork with a glowing heart"></div><div class="abs product-name">Love Spell</div><div class="abs product-meta">psychic<b>$200.00</b></div></div>
    <div class="abs product" style="left:196px;top:795px"><div class="abs product-art" role="img" aria-label="Love Spells product artwork with a glowing heart"></div><div class="abs product-name">Love Spell</div><div class="abs product-meta">psychic<b>$200.00</b></div></div>
    <div class="abs product" style="left:295px;top:795px"><div class="abs product-art" role="img" aria-label="Love Spells product artwork with a glowing heart"></div><div class="abs product-name">Love Spell</div><div class="abs product-meta">psychic<b>$200.00</b></div></div>
    <div class="abs product" style="left:394px;top:795px"><div class="abs product-art" role="img" aria-label="Love Spells product artwork with a glowing heart"></div><div class="abs product-name">Love Spell</div><div class="abs product-meta">psychic<b>$200.00</b></div></div>
  </section>

  <aside>
    <div class="abs side-box" style="top:543px;height:124px">
      <div class="abs side-title newsletter-title">Newsletter</div>
      <div class="abs side-rule" style="left:9px;top:30px;width:117px"></div>
      <p class="abs newsletter-copy">Lorem ipsum dolor sit amet, con-<br>sectetuer adipiscing elit.</p>
      <div class="abs email-field">Your Email</div>
      <div class="abs btn-submit">Submit</div>
    </div>

    <div class="abs side-box" style="top:681px;height:207px">
      <div class="abs side-title video-title">How to be psychic, have intu-<br>ition, and do mind reading</div>
      <div class="abs video-thumb" role="img" aria-label="Video still of a smiling presenter">
        <svg class="abs" style="left:51px;top:36px" width="14" height="14" viewBox="0 0 14 14"><path d="M3 1l10 6-10 6z" fill="#fff"/></svg>
      </div>
      <div class="abs side-rule" style="left:9px;top:136px;width:117px"></div>
      <p class="abs video-copy">Learn more about lorem ipsum<br>dolor sit amet, consectetuer<br>adipiscing elit. Aenean com-<br>modo ligula eget dolor.</p>
    </div>

    <div class="abs side-box" style="top:912px;height:208px">
      <div class="abs join-avatar"></div>
      <div class="abs join-title">Are you PSYCHIC?</div>
      <p class="abs join-copy">Do you want to be<strong>ONE OF US</strong>lorem ipsum dolor sit amet, consectetuer adipiscing elit. Aenean commodo ligula eget dolor.</p>
      <div class="abs btn-join">Join Now</div>
    </div>
  </aside>

  <section class="about">
    <h2 class="abs section-title" style="left:99px;top:911px;width:388px">Little bit About Us</h2>
    <div class="abs about-copy">
      <p>If you have an issue in your life that is causing you any sort of distress, no matter what it is, a read-<br>ing from one of our psychics will give you immediate, compassionate insight. There are moments<br>when you need more answers than you can get on your own. That's why the gifted psychics at<br>Lantern of Seers are here for you, 24/7.</p>
      <p>Maybe your relationship suddenly fell apart and you don't know why. Perhaps you just lost a loved<br>one and want to contact them. Maybe you suffered an unexpected financial crisis and you need to<br>make a critical decision.</p>
      <p>All of our psychics are vetted before they come on board, so you don't have to spend critical time<br>searching for someone you can trust. Many are born psychics, or developed their gifts at an early<br>age, and come from backgrounds where these gifts run in their families. They all have many tools<br>and abilities and they all love using their gifts to help people.</p>
    </div>
  </section>

  <footer>
    <div class="abs footer-rule"></div>
    <div class="abs footer-links">Home<span>|</span>Psychic<span>|</span>Marketplace<span>|</span>My account</div>
    <div class="abs footer-copy">Copyright © 2013 Seerhall, Inc.  All rights reserved</div>
  </footer>
</div>
</body>
</html>
```